Luminously Grounded Vitality

We want to design a business card that is modern and appealing for an innovative psychedelic telemedicine company that provides at-home ketamine-assisted therapy along with wellness, longevity, and anti-aging medicines. We want to use our deep purple and white plus other colors you can find on our website. We don't have any strict brand guidelines yet so feel free to get creative. We want a very professional, but technology first modern design that will instill trust, peace, calm, but also be attractive to investors in the healthcare and SaaS space.

```html
<!DOCTYPE html>
<html lang="en">
<head>
<meta charset="UTF-8">
<title>Luminously Grounded Vitality – Business Card</title>
<link rel="stylesheet" href="https://fonts.googleapis.com/css2?family=Varela+Round&family=Roboto:wght@400;500&display=swap">
<style>
  :root {
    --bg: #1f1f1f;
    --paper: #ffffff;
    --orchid: #b270a2;
    --violet: #7f6aab;
    --ink: #1c1c1c;
    --card-w: 600px;
    --card-h: 343px;
  }
  * { box-sizing: border-box; margin: 0; padding: 0; }
  html, body { width: 1200px; height: 1015px; overflow: hidden; }
  body {
    background: var(--bg);
    display: flex;
    flex-direction: column;
    align-items: center;
    justify-content: center;
    gap: 70px;
    font-family: "Roboto", sans-serif;
  }
  .card {
    position: relative;
    width: var(--card-w);
    height: var(--card-h);
    background: var(--paper);
    overflow: hidden;
  }
  .band {
    position: absolute;
    left: 0; right: 0; bottom: 0;
    top: 57%;
  }
  .card--front .band { background: var(--orchid); }
  .card--back .band { background: var(--violet); }

  .icon-badge {
    position: absolute;
    width: 58px; height: 58px;
    border-radius: 50%;
    border: 4px solid var(--paper);
    display: flex; align-items: center; justify-content: center;
    transform: translate(-50%, -50%);
    top: 57%;
  }
  .card--front .icon-badge { background: var(--orchid); left: 47%; }
  .card--back .icon-badge { background: var(--violet); }
  .icon-badge svg { width: 26px; height: 26px; }

  .brand {
    position: absolute;
    left: 0; right: 0; top: 26%;
    display: flex; align-items: center; justify-content: center; gap: 14px;
  }
  .brand-dot {
    width: 26px; height: 26px; border-radius: 50%;
    background: var(--violet);
  }
  .brand-name {
    font-family: "Varela Round", sans-serif;
    color: var(--orchid);
    font-size: 33px;
    letter-spacing: 0.5px;
  }

  .person {
    position: absolute;
    left: 0; right: 0; top: 18%;
    text-align: center;
    padding-left: 60px;
  }
  .person-name {
    font-family: "Varela Round", sans-serif;
    color: var(--orchid);
    font-size: 40px;
    line-height: 1;
  }
  .person-title {
    margin-top: 4px;
    color: var(--ink);
    font-size: 19px;
    letter-spacing: 0.5px;
  }
  .contact {
    position: absolute;
    top: 75%;
    color: var(--paper);
    font-size: 15px;
    letter-spacing: 0.3px;
    transform: translateX(-50%);
    white-space: nowrap;
  }
  .badge--email, .contact--email { left: 20%; }
  .badge--phone, .contact--phone { left: 50%; }
  .badge--web, .contact--web { left: 80%; }
</style>
</head>
<body>

<section class="card card--front" aria-label="Card front">
  <div class="brand">
    <span class="brand-dot"></span>
    <span class="brand-name">Luminously Grounded Vitality</span>
  </div>
  <div class="band"></div>
  <div class="icon-badge" aria-label="Location">
    <svg viewBox="0 0 24 24" fill="none">
      <path d="M12 2.5c-3.9 0-7 3-7 6.8 0 4.8 7 12.2 7 12.2s7-7.4 7-12.2c0-3.8-3.1-6.8-7-6.8z" fill="#fff"/>
      <circle cx="12" cy="9.3" r="2.6" fill="var(--orchid)"/>
    </svg>
  </div>
</section>

<section class="card card--back" aria-label="Card back">
  <div class="person">
    <div class="person-name">Daniel Hartwell</div>
    <div class="person-title">Managing Director</div>
  </div>
  <div class="band"></div>

  <div class="icon-badge badge--email" aria-label="Email">
    <svg viewBox="0 0 24 24" fill="none">
      <rect x="2.5" y="5" width="19" height="14" rx="1" fill="#fff"/>
      <path d="M3 6l9 7 9-7M3 18.5l7-6M21 18.5l-7-6" stroke="var(--violet)" stroke-width="1.4"/>
    </svg>
  </div>
  <div class="icon-badge badge--phone" aria-label="Phone">
    <svg viewBox="0 0 24 24" fill="none">
      <path d="M6.6 3.5l2.6 3.6-1.6 2c1.2 2.6 3 4.4 5.6 5.6l2-1.6 3.6 2.6-1.4 3.2C10.6 19.2 4.8 13.4 3.4 6.6z" fill="#fff"/>
      <path d="M14 4.5a6 6 0 0 1 5.5 5.5M13.6 7.6a3 3 0 0 1 2.8 2.8" stroke="#fff" stroke-width="1.6" stroke-linecap="round"/>
    </svg>
  </div>
  <div class="icon-badge badge--web" aria-label="Website">
    <svg viewBox="0 0 24 24" fill="none" stroke="#fff" stroke-width="1.6">
      <circle cx="12" cy="12" r="9"/>
      <ellipse cx="12" cy="12" rx="4" ry="9"/>
      <path d="M3 12h18M4.5 7.5h15M4.5 16.5h15"/>
    </svg>
  </div>

  <div class="contact contact--email">hello@groundedvitality.com</div>
  <div class="contact contact--phone">044-987 654 321</div>
  <div class="contact contact--web">www.groundedvitality.com</div>
</section>

</body>
</html>
```